The Orchard Gate

The Design Brief and Flyer Text are in Documents attached
Other design components also attached
Only allowed five doc attachments - so please use the first pic of sculpture for the remaining three and then once design is finalised I can send you the other pics for the print ready files
Many thanks
Tom Harland
tom@velmora4.com
01632 480517

```html
<!DOCTYPE html>
<html lang="en">
<head>
<meta charset="utf-8">
<title>The Quiet Return – Silent Walking Meditation</title>
<link rel="stylesheet" href="https://fonts.googleapis.com/css2?family=Open+Sans:wght@400;600;700&family=Questrial&display=swap">
<style>
:root{
  --paper:#ffffff;
  --ink:#111111;
  --mark:#9a9a9a;
  --art-light:#e9e9e9;
  --art-dark:#bdbdbd;
  --photo-green:#5d7a3e;
  --photo-stone:#c9c4b8;
}
*{margin:0;padding:0;box-sizing:border-box}
html,body{width:1200px;height:399px;overflow:hidden;background:var(--paper)}
body{font-family:"Questrial",sans-serif;color:var(--ink)}
.sheet{position:relative;width:1200px;height:399px}
.panel{position:absolute;top:0;height:399px}
.crop{position:absolute;width:8px;height:8px;border-color:var(--mark);border-style:solid;border-width:0}
.crop.tl{border-left-width:1px;border-top-width:1px}
.crop.tr{border-right-width:1px;border-top-width:1px}
.crop.bl{border-left-width:1px;border-bottom-width:1px}
.crop.br{border-right-width:1px;border-bottom-width:1px}

/* Cover */
.cover{left:0;width:300px;text-align:center}
.cover-title{position:absolute;top:2px;left:0;width:300px;font-size:29px;font-weight:400;white-space:nowrap}
.cover-art{position:absolute;left:30px;top:44px;width:250px;height:228px}
.cover-heading{position:absolute;top:273px;left:0;width:300px;font-family:"Open Sans",sans-serif;font-size:21px;font-weight:600;line-height:24px}
.cover-note{position:absolute;top:322px;left:0;width:300px;font-size:19px;line-height:21px}

/* Inside spread */
.inside{left:320px;width:580px}
.inside-title{text-align:center;font-size:14px;font-weight:400;margin-top:9px;line-height:17px}
.intro{font-size:7.8px;line-height:9.6px;margin:2px 4px 0 10px}
.intro p+p{margin-top:7px}
.col{position:absolute;width:278px}
.col.left{left:10px;top:124px}
.col.right{left:292px;top:124px}
.stage{position:relative;height:89px;padding-right:62px;font-size:7.8px;line-height:9.6px}
.stage h3{font-family:"Open Sans",sans-serif;font-size:8.4px;font-weight:600;text-decoration:underline;line-height:10px}
.stage .photo{position:absolute;right:2px;top:0;width:52px;height:80px}

/* Journey panel */
.journey{left:908px;width:292px}
.journey-title{text-align:center;font-family:"Open Sans",sans-serif;font-size:16px;font-weight:700;margin-top:10px;line-height:19px}
.journey-sub{text-align:center;font-family:"Open Sans",sans-serif;font-size:9px;font-weight:600;line-height:11px}
.step{margin:0 14px 0 10px;font-size:9px;line-height:11px}
.step h3{font-family:"Open Sans",sans-serif;font-size:8.6px;font-weight:700;text-decoration:underline;line-height:11px}
.step ul{list-style:none}
.step li{padding-left:8px;position:relative}
.step li::before{content:"•";position:absolute;left:0}
.step.inward{margin-top:40px}
.step.centre{margin-top:14px}
.step.outward{margin-top:12px}
.credits{position:absolute;top:322px;left:0;width:292px;text-align:center}
.credits .host{font-size:11px;line-height:13px}
.credits .venue{font-size:8.4px;line-height:10px}
.credits .makers{font-size:8.4px;line-height:10.5px;margin-top:10px}
</style>
</head>
<body>
<div class="sheet">

  <section class="panel cover">
    <span class="crop tl" style="left:4px;top:4px"></span>
    <span class="crop bl" style="left:4px;bottom:4px"></span>
    <span class="crop br" style="right:4px;bottom:4px"></span>
    <span class="crop tr" style="right:4px;top:4px"></span>
    <h1 class="cover-title">The Quiet Return</h1>
    <svg class="cover-art" viewBox="0 0 250 228" role="img" aria-label="Illustration of a stone archway standing over a spiral labyrinth">
      <defs>
        <linearGradient id="art-fade" x1="0" y1="0" x2="0" y2="1">
          <stop offset="0" stop-color="var(--art-light)"/>
          <stop offset="1" stop-color="var(--art-dark)"/>
        </linearGradient>
      </defs>
      <rect width="250" height="228" fill="url(#art-fade)"/>
    </svg>
    <h2 class="cover-heading">The Orchard Gate<br>Silent Walking Meditation</h2>
    <p class="cover-note">Don’t forget to walk The Orchard Gate and rediscover your SELF at the top of the gardens</p>
  </section>

  <section class="panel inside">
    <span class="crop tl" style="left:-6px;top:4px"></span>
    <span class="crop bl" style="left:-6px;bottom:4px"></span>
    <span class="crop tr" style="right:0;top:4px"></span>
    <span class="crop br" style="right:0;bottom:4px"></span>
    <h2 class="inside-title">The Quiet Return</h2>
    <div class="intro">
      <p>A Labyrinth is an ancient human symbol for the journey of spiritual awakening. It is not a maze. It has no dead ends, no choices and no corners. As you ‘meander’ you contemplate in silence who and what you ‘really’ are. You review and throw off all the old ideas about your self along the way, while gently realising your true spiritual nature. By the time you reach the centre you have freed your self from all mental illusions and emotional burdens. The authentic and unconditioned self has awoken. You have realised who you really are - the spiritual being animating and playing through a human form. Soul not body! You are able to be your ‘true self’ again. And that changes almost everything!</p>
      <p>As you stop at the six different standing sculptures, contemplate<br>what they mean to you. There is no one right interpretation as we all<br>awaken to who and what we are in our own way. Here is one<br>interpretation reflecting the creators inspirations.</p>
    </div>

    <div class="col left">
      <article class="stage">
        <h3>Self AWARENESS</h3>
        <p>I am. Soul - I am Light - I am Love<br>Take a moment to contemplate a<br>different way of ‘seeing’ your self. Take a moment to ‘consider’ your self to be a soul, a spiritual being. Now hold that gently at the back of your awareness as you meander silently to the centre of The Orchard Gate</p>
        <svg class="photo" viewBox="0 0 52 80" role="img" aria-label="Photo of a carved stone sculpture in a garden"><rect width="52" height="80" fill="var(--photo-green)"/><rect x="19" y="6" width="14" height="70" fill="var(--photo-stone)"/></svg>
      </article>
      <article class="stage">
        <h3>Self DISCOVERY</h3>
        <p>Each day there are contrasting and conflicting thoughts and feelings within. Some light and some dark. There is virtue and vice. The virtues of my character are like gold. They are ‘real’ and forever. The vices within my character are like ghosts, dark and temporary.</p>
        <svg class="photo" viewBox="0 0 52 80" role="img" aria-label="Photo of a carved stone sculpture in a garden"><rect width="52" height="80" fill="var(--photo-green)"/><rect x="19" y="6" width="14" height="70" fill="var(--photo-stone)"/></svg>
      </article>
      <article class="stage">
        <h3>Self UNDERSTANDING</h3>
        <p>The reality is that while my thoughts and feelings may change the ‘real’ me<br>cannot change. I will be again what I always was. I am the eternal being. I can only realise this for my self from the inside! (hence the back to front wording on the stone)</p>
        <svg class="photo" viewBox="0 0 52 80" role="img" aria-label="Photo of a carved stone sculpture in a garden"><rect width="52" height="80" fill="var(--photo-green)"/><rect x="19" y="6" width="14" height="70" fill="var(--photo-stone)"/></svg>
      </article>
    </div>

    <div class="col right">
      <article class="stage">
        <h3>Self MASTERY</h3>
        <p>Victory and Faith.<br>Each day is filled with victory and defeat. I know defeat when I react emotionally. I know Victory when I consciously respond from a state of inner peace and with love, even when challenged and tested by others. My Faith is sustained when I drink from ‘the inner grail’ in which I can always find my peace and my capacity to love. This is ‘the grail’ of my true nature.</p>
        <svg class="photo" viewBox="0 0 52 80" role="img" aria-label="Photo of a carved stone sculpture in a garden"><rect width="52" height="80" fill="var(--photo-green)"/><rect x="19" y="6" width="14" height="70" fill="var(--photo-stone)"/></svg>
      </article>
      <article class="stage">
        <h3>Self WORTH</h3>
        <p>I want NOMORE. I crave NOMORE. I need NOMORE. The old me who used to think ‘my wealth was my worth’ is NOMORE. ALL the old me’s have died. I can see the true worth and beauty of the real me starting to grow and blossom.</p>
        <svg class="photo" viewBox="0 0 52 80" role="img" aria-label="Photo of a carved stone sculpture in a garden"><rect width="52" height="80" fill="var(--photo-green)"/><rect x="19" y="6" width="14" height="70" fill="var(--photo-stone)"/></svg>
      </article>
      <article class="stage">
        <h3>Self REALISATION</h3>
        <p>Om. I am.<br>Now I know my self as no one other than the ‘I’ that says, “I am”. This is the true me. Free of all the other false ‘me’s’ I can now walk back into the world as the authentic self and just be... my self.</p>
        <svg class="photo" viewBox="0 0 52 80" role="img" aria-label="Photo of a carved stone sculpture in a garden"><rect width="52" height="80" fill="var(--photo-green)"/><rect x="19" y="6" width="14" height="70" fill="var(--photo-stone)"/></svg>
      </article>
    </div>
  </section>

  <section class="panel journey">
    <span class="crop tl" style="left:4px;top:4px"></span>
    <span class="crop bl" style="left:4px;bottom:4px"></span>
    <span class="crop tr" style="right:4px;top:4px"></span>
    <span class="crop br" style="right:4px;bottom:4px"></span>
    <h2 class="journey-title">The Quiet Return</h2>
    <p class="journey-sub">A SILENT journey in three stages</p>

    <div class="step inward">
      <h3>The Journey Inward</h3>
      <ul>
        <li>Walk slowly to the centre - at least half the pace you normally walk</li>
        <li>Stop for a few moments at each of the six stone sculptures</li>
        <li>Contemplate what each one means to you - see what it awakens within you</li>
      </ul>
    </div>
    <div class="step centre">
      <h3>At the Centre</h3>
      <ul>
        <li>Stop and just be in complete silence</li>
        <li>Meditate on I AM</li>
        <li>Be silent - be still - just be the ‘I’ that says, “I am”.</li>
      </ul>
    </div>
    <div class="step outward">
      <h3>The Journey Outwards</h3>
      <ul>
        <li>As you return you take the same path at the same pace but you now feel different</li>
        <li>You return to the world with a new state of being</li>
        <li>As you walk visualise what you might do differently when you arrive back in the world of action and interaction!</li>
      </ul>
    </div>

    <div class="credits">
      <p class="host">Calm in the Meadow</p>
      <p class="venue">Hillside Quiet Centre</p>
      <p class="makers">The Orchard Gate Designed and Created by - Alan Pryce<br>Sculptures Created by - Ivo Lannert</p>
    </div>
  </section>

</div>
</body>
</html>
```